Talon Microchips PowerPoint Master Slide Deck Design

This is a 2-phase project to design a slide deck for a semiconductor company in the Silicon Valley. The design budget will be increased with each phase.
The slide deck will need to have one version with a dark background for presentations and a second version with a white background. Otherwise, the slides will be the same. I anticipate we will need a total of 10 slides, but that number may change.
The first phase will be to design a Title and a Title and Content slide.
- The Title Slide is the first slide of the deck. It should include the presentation title, the presenter's name and date of presentation
- The Title and Content slide should include a title and content with bullet points and up to 2 additional sub-bullets
- The Title and Content slide should have a footer that includes the slide #, Talon Microchips Confidential, and the logo. This footer will be on every slide except the Title Slide
The first two slides will serve as the format for the remaining ~8 slides:
-Header and Content Text (1, 2, 4 column)
-Header and Content Image (bar chart, pie chart, tables)
-Break
-Title only
-Closing (Talon logo only)
Our slides contain a lot of content so a clean and simple design is best.
Both phases will need to include pre-set color options for
-Text and Lines
-Shadows
-Bullets and sub-bullets (including shapes, ex. circle, slash, square, etc.)
-Bar charts, pie charts, tables
Samples of our collateral are attached. Logo files are also attached

```html
<!DOCTYPE html>
<html lang="en">
<head>
<meta charset="utf-8">
<title>Talon Microchips – Master Slide Deck</title>
<link rel="stylesheet" href="https://fonts.googleapis.com/css2?family=Montserrat:wght@400;500;600;800&family=Yellowtail&display=swap">
<style>
  :root{
    --page:#e9eaec;
    --slide:#3a3a3a;
    --ink:#ffffff;
    --muted:#d6d6d6;
    --blue:#1746ff;
    --blue-mid:#0a6cff;
    --cyan:#1ec8ff;
    --deep:#0d2bd6;
    --line:#8a8a8a;
  }
  *{box-sizing:border-box;margin:0;padding:0}
  html,body{width:1200px;height:4926px;overflow:hidden}
  body{background:var(--page);font-family:"Montserrat",sans-serif;color:var(--ink);position:relative}

  .brand-hero{position:absolute;top:300px;left:0;width:1200px;text-align:center;
    font-weight:600;font-size:46px;color:#2a2a2a;letter-spacing:1px}
  .brand-hero .dot{display:inline-block;width:22px;height:22px;border-radius:50%;
    background:var(--blue);margin-right:14px;vertical-align:middle}

  .slide{position:absolute;left:240px;width:720px;height:397px;background:var(--slide);overflow:hidden}
  .slide::after{content:"";position:absolute;left:0;right:0;bottom:0;height:7px;
    background:linear-gradient(90deg,var(--deep),var(--blue-mid) 60%,var(--cyan))}

  .title{position:absolute;font-weight:800;font-size:40px;line-height:1;text-transform:uppercase;letter-spacing:.5px}
  .body{position:absolute;font-size:11px;line-height:1.4;color:var(--muted)}
  .center{left:0;right:0;text-align:center}

  .footer{position:absolute;left:241px;bottom:22px;display:flex;align-items:center;gap:18px}
  .footer .conf{font-size:8px;color:var(--muted)}
  .footer .mark{font-size:11px;font-weight:600;display:flex;align-items:center;gap:5px}
  .footer .mark::before{content:"";width:8px;height:8px;border-radius:50%;background:var(--blue)}

  .art{position:absolute}
  .art-circuit{background:radial-gradient(circle at 60% 35%,var(--blue-mid),var(--deep) 70%,transparent 72%)}
  .art-photo{background:linear-gradient(135deg,#6b6b6b,#2b2b2b)}
  .art-blue-photo{background:radial-gradient(ellipse at 45% 50%,#3d7bff,var(--deep) 70%);border-radius:40px}

  .avatar{position:absolute;left:554px;top:183px;width:84px;height:84px;border-radius:50%;
    border:3px solid #fff;background:linear-gradient(160deg,#9a8a7a,#4a4a4a)}
  .presenter{position:absolute;left:516px;top:262px;width:160px;text-align:center;font-size:19px;line-height:1.2;color:var(--muted)}
  .date{position:absolute;left:65px;top:364px;font-size:13px;color:var(--muted)}

  .bullets{position:absolute;left:52px;top:175px;list-style:none}
  .bullets > li{position:relative;padding-left:44px;margin-bottom:30px}
  .bullets > li::before{content:"";position:absolute;left:0;top:0;width:28px;height:28px;border-radius:50%;
    border:3px solid var(--blue-mid);box-shadow:inset 0 0 0 5px var(--slide),inset 0 0 0 9px var(--cyan)}
  .bullets .head{font-weight:600;font-size:17px;display:block;margin-bottom:6px}
  .bullets .sub{list-style:none}
  .bullets .sub li{font-size:13px;color:var(--muted);padding-left:20px;position:relative;line-height:1.55}
  .bullets .sub li::before{content:"✓";position:absolute;left:0;top:1px;width:13px;height:13px;border:1px solid var(--muted);
    border-radius:50%;font-size:8px;line-height:12px;text-align:center}

  .chart-bars{position:absolute;left:376px;top:150px}
  .break-pill{position:absolute;left:304px;top:142px;width:256px;height:84px;border:1.5px solid var(--blue-mid);border-radius:42px;
    font-family:"Yellowtail",cursive;font-size:66px;line-height:80px;padding-left:20px;color:#fff}
  .closing-mark{position:absolute;top:150px;left:0;right:0;text-align:center;font-weight:600;font-size:44px}
  .closing-mark .dot{display:inline-block;width:24px;height:24px;border-radius:50%;background:var(--blue);margin-right:14px;vertical-align:middle}
</style>
</head>
<body>

<div class="brand-hero"><span class="dot"></span>Talon Microchips</div>

<!-- Title slide -->
<section class="slide" style="top:875px">
  <div class="art art-circuit" style="left:466px;top:-20px;width:254px;height:205px" role="img" aria-label="Blue circuit-trace decoration"></div>
  <h1 class="title" style="left:65px;top:128px">Presentation<br>Title</h1>
  <div class="avatar" role="img" aria-label="Presenter portrait"></div>
  <p class="presenter">Presenter's<br>Name</p>
  <p class="date">12-12-2023</p>
</section>

<!-- Title and content -->
<section class="slide" style="top:1315px">
  <div class="art art-photo" style="left:432px;top:0;width:288px;height:386px" role="img" aria-label="Black and white photo of two colleagues at a laptop"></div>
  <div class="art art-circuit" style="left:367px;top:-20px;width:194px;height:150px" role="img" aria-label="Blue circuit-trace decoration"></div>
  <h2 class="title" style="left:52px;top:42px">Slide Title</h2>
  <p class="body" style="left:52px;top:86px;width:290px;font-size:9px">Lorem ipsum dolor sit amet, consectetuer adipiscing elit, sed diam nonummy nibh euismod tincidunt ut laoreet dolore magna aliquam erat volutpat. Ut wisi enim ad minim veniam, quis nostrud exerci tation ullamcorper suscipit lobortis nisl ut aliquip ex ea</p>
  <ul class="bullets">
    <li><span class="head">Bullet Point 1</span><ul class="sub"><li>Sub-bullet point</li><li>Sub-bullet point</li></ul></li>
    <li><span class="head">Bullet Point 1</span><ul class="sub"><li>Sub-bullet point</li><li>Sub-bullet point</li></ul></li>
  </ul>
  <div class="footer"><span class="conf">#Talon Microchips Confidential</span><span class="mark">TALON</span></div>
</section>

<!-- Image left -->
<section class="slide" style="top:1754px">
  <div class="art art-blue-photo" style="left:0;top:52px;width:256px;height:288px" role="img" aria-label="Blue-tinted team photo in circuit shape"></div>
  <h2 class="title" style="left:323px;top:105px">Slide Title</h2>
  <p class="body" style="left:323px;top:150px;width:320px;font-size:12px">Lorem ipsum dolor sit amet, consectetuer adipiscing elit, sed diam nonummy nibh euismod tincidunt ut laoreet dolore magna aliquam erat volutpat. Ut wisi enim ad minim veniam, quis nostrud exerci tation ullamcorper suscipit lobortis nisl ut aliquip ex ea</p>
  <div class="footer"><span class="conf">#Talon Microchips Confidential</span><span class="mark">TALON</span></div>
</section>

<!-- Centered text -->
<section class="slide" style="top:2192px">
  <h2 class="title center" style="top:117px">Slide Title</h2>
  <p class="body center" style="top:166px;margin:0 auto;width:440px;font-size:12px">Lorem ipsum dolor sit amet, consectetuer adipiscing elit, sed diam nonummy nibh euismod tincidunt ut laoreet dolore magna aliquam erat volutpat. Ut wisi enim ad minim veniam, quis nostrud exerci tation ullamcorper suscipit lobortis nisl ut aliquip ex ea</p>
  <div class="footer"><span class="conf">#Talon Microchips Confidential</span><span class="mark">TALON</span></div>
</section>

<!-- Image right -->
<section class="slide" style="top:2631px">
  <div class="art art-blue-photo" style="left:441px;top:50px;width:262px;height:290px" role="img" aria-label="Blue-tinted team photo in circuit shape"></div>
  <h2 class="title" style="left:75px;top:102px">Slide Title</h2>
  <p class="body" style="left:75px;top:146px;width:310px;font-size:12px">Lorem ipsum dolor sit amet, consectetuer adipiscing elit, sed diam nonummy nibh euismod tincidunt ut laoreet dolore magna aliquam erat volutpat. Ut wisi enim ad minim veniam, quis nostrud exerci tation ullamcorper suscipit lobortis nisl ut aliquip ex ea</p>
  <div class="footer"><span class="conf">#Talon Microchips Confidential</span><span class="mark">TALON</span></div>
</section>

<!-- Charts -->
<section class="slide" style="top:3069px">
  <h2 class="title center" style="top:28px">Slide Title</h2>
  <p class="body center" style="top:78px;margin:0 auto;width:470px;font-size:11px">Lorem ipsum dolor sit amet, consectetuer adipiscing elit, sed diam nonummy nibh euismod tincidunt ut laoreet dolore magna aliquam erat volutpat. Ut wisi enim ad minim veniam, quis nostrud exerci tation ullam-</p>
  <svg class="art" style="left:135px;top:155px" width="184" height="184" viewBox="-92 -92 184 184" aria-label="Donut chart">
    <defs><linearGradient id="g-blue" x1="0" y1="0" x2="1" y2="1"><stop offset="0" stop-color="#1ec8ff"/><stop offset="1" stop-color="#1746ff"/></linearGradient></defs>
    <g fill="none" stroke-width="46" transform="rotate(-90)">
      <circle r="66" stroke="#ffffff" stroke-dasharray="82.9 414.7" stroke-dashoffset="0" transform="rotate(-72)"/>
      <circle r="66" stroke="url(#g-blue)" stroke-dasharray="20.7 414.7"/>
      <circle r="66" stroke="#1746ff" stroke-dasharray="62.2 414.7" transform="rotate(18)"/>
      <circle r="66" stroke="#ffffff" stroke-dasharray="82.9 414.7" transform="rotate(72)"/>
      <circle r="66" stroke="url(#g-blue)" stroke-dasharray="165.9 414.7" transform="rotate(144)"/>
    </g>
    <g font-family="Montserrat,sans-serif" font-size="9" font-weight="600" text-anchor="middle">
      <text x="-50" y="-36" fill="#333">20%</text>
      <text x="-8" y="-54" fill="#fff">5%</text>
      <text x="44" y="-18" fill="#fff">15%</text>
      <text x="38" y="50" fill="#333">20%</text>
      <text x="-52" y="34" fill="#fff">40%</text>
    </g>
  </svg>
  <svg class="chart-bars" width="210" height="200" viewBox="0 0 210 200" aria-label="Bar chart 2018 to 2022">
    <defs><linearGradient id="g-bar" x1="0" y1="0" x2="0" y2="1"><stop offset="0" stop-color="#1ec8ff"/><stop offset="1" stop-color="#1746ff"/></linearGradient></defs>
    <g font-family="Montserrat,sans-serif" font-size="9" font-weight="600">
      <rect x="0" y="53" width="20" height="92" rx="10" fill="#fff"/>
      <rect x="42" y="7" width="20" height="138" rx="10" fill="url(#g-bar)"/>
      <rect x="86" y="41" width="20" height="104" rx="10" fill="#fff"/>
      <rect x="130" y="24" width="20" height="121" rx="10" fill="url(#g-bar)"/>
      <rect x="174" y="80" width="20" height="65" rx="10" fill="#fff"/>
      <text transform="translate(14 128) rotate(-90)" fill="#333">45%</text>
      <text transform="translate(56 128) rotate(-90)" fill="#fff">75%</text>
      <text transform="translate(100 128) rotate(-90)" fill="#333">50%</text>
      <text transform="translate(144 128) rotate(-90)" fill="#fff">60%</text>
      <text transform="translate(188 128) rotate(-90)" fill="#333">22%</text>
      <g fill="#fff" text-anchor="middle" font-size="7">
        <text x="10" y="161">2018</text><text x="52" y="161">2019</text><text x="96" y="161">2020</text><text x="140" y="161">2021</text><text x="184" y="161">2022</text>
      </g>
      <g fill="#bbb" text-anchor="middle" font-size="4.5" font-weight="400">
        <text x="10" y="170">Lorem ipsum</text><text x="52" y="170">Lorem ipsum</text><text x="96" y="170">Lorem ipsum</text><text x="140" y="170">Lorem ipsum</text><text x="184" y="170">Lorem ipsum</text>
      </g>
    </g>
  </svg>
  <div class="footer"><span class="conf">#Talon Microchips Confidential</span><span class="mark">TALON</span></div>
</section>

<!-- Break -->
<section class="slide" style="top:3508px">
  <div class="break-pill">Break</div>
  <div class="art" style="left:155px;top:94px;width:150px;height:147px;border-radius:20px;background:linear-gradient(180deg,#d9d9d9,#8a8a8a)" role="img" aria-label="Coffee mug illustration"></div>
  <div class="footer"><span class="conf">#Talon Microchips Confidential</span><span class="mark">TALON</span></div>
</section>

<!-- Title only -->
<section class="slide" style="top:3946px">
  <div class="art art-circuit" style="left:495px;top:-20px;width:225px;height:160px" role="img" aria-label="Blue circuit-trace decoration"></div>
  <h2 class="title center" style="top:153px">Slide Title</h2>
  <div class="footer"><span class="conf">#Talon Microchips Confidential</span><span class="mark">TALON</span></div>
</section>

<!-- Closing -->
<section class="slide" style="top:4386px">
  <div class="closing-mark"><span class="dot"></span>Talon Microchips</div>
  <div class="footer"><span class="conf">#Talon Microchips Confidential</span><span class="mark">TALON</span></div>
</section>

</body>
</html>
```